Hunting business need a new wild boar hunting flyer

We need a flyer design for a company based in Saint-Hénédine, Québec. We are a hunting preserve and this flyer must be made for the Boar hunting market. we don’t have any particular restriction for the format but would prefer a tri-fold. The flyer is intended to be given to customer during trade show. You don’t need to put all the information on the flyer I know I have put a lot of info.

85% of our customer are Male with high school or college scholarship.

I may be wrong, but I would like the flyer to have lot’s of black and with a tough style almost like a biker style. Something not clean and hard but with a professional design.

We don’t do standard, don’t be affraid to submit something special even if it required manual assembling. We need something that will mark the customer in the trade show. Note that the custommer receive at least 30 flyers from competitors as well.

Logo of the company in the files.
See files for photo of wild boar.
Would be nice to add wild boar, wild boar skull are pretty impressive (it’s sanglier in french)

Sample text :

Montrez votre côté rebelle!

Offrez-vous LE trip de chasse entre amis !

Chassez en tout temps et sans permis sur deux magnifiques territoires forestiers de la taille de 30 terrains de football chacun. Les enclos sont situés en Beauce, à 30 minutes de Québec. Le taux de succès est de 100 %. Nous pouvons aussi fournir l'hébergement sur demande. La ferme est ouverte depuis 1982 et a toujours été gérée par des passionnés de la chasse, de la nature et de la bonne venaison.

C’est presque « hors-la-loi »!
• Aucun permis requis
• Succès garanti
• Chasse pendant toute l’année
• Guide sur place et territoire exclusif
• À proximité de Québec

Intense et renversant!

Que vous soyez un chasseur débutant ou vétéran, la chasse au sanglier sera pour vous une expérience extraordinaire. Ce gibier, qui ne vit pas à l’état sauvage au Québec, est un adversaire de taille. Ne vous fiez pas à son allure tranquille. S’il se sent en danger, il n’hésite pas à se sauver à toute vitesse et il n’arrête pas, même si vous vous trouvez sur son chemin. Ce gibier est suffisamment gros pour être chassé avec la plupart des carabines. Il se prête aussi très bien à la chasse au fusil, à l’arc ou à l’arbalète.

C’est bien beau, mais ça goûte quoi?

La chair du sanglier est rouge et elle est plus maigre que celle du porc. Elle est très tendre et succulente. Le sanglier offre les mêmes possibilités de coupe que le porc. Vous pouvez aussi l’essayer en méchoui à l’occasion d’une rencontre de groupe. Vos convives et vous dégusterez alors une venaison exceptionnelle.

Quelques commentaires de nos chasseurs :

« J’ai été surpris de voir à quel point ces animaux peuvent se cacher et se déplacer rapidement. C’est beaucoup plus difficile que je croyais. »
Gaston, Québec, 2015

« La viande était succulente et tendre. J’ai hâte de revenir récolter un autre sanglier à la ferme. »
Brigitte, Québec, 2015

Réservez pendant le salon et obtenez le crâne blanchi de votre sanglier gratuitement.

Venez récolter les espèces exotiques suivantes :
Cerf de Virginie (500 $*)
Cerf élaphe (850 $*)
Sika (600 $*)
Daim (500 $*)
Dindon sauvage (85 $*)
Faisan (200 $ pour 10)
Sanglier (350 $*)

*Prix de départ, sujet à changement sans préavis.

Le Domaine des Ronces
418, rang des Érables
Sainte-Hénédine (Québec) G0M 4K7

Tél. : 418 555-0147
Courriel : info@ronceviel.farm
Site Web : www.ronceviel.farm

See description

Hunting

Must have
• Hard, rebel or dirty look.

```html
<!DOCTYPE html>
<html lang="fr">
<head>
<meta charset="utf-8">
<title>Chasse au sanglier — dépliant</title>
<link rel="stylesheet" href="https://fonts.googleapis.com/css2?family=Open+Sans:ital,wght@0,400;0,600;0,700;1,400;1,600;1,700&display=swap">
<style>
  :root {
    --page-bg: #f2f2f2;
    --panel-black: #0b0b0b;
    --panel-edge: #1c1c1c;
    --text-light: #d9d9d9;
    --text-heading: #f2f2f2;
    --text-muted: #a8a8a8;
    --forest-dark: #2a2418;
    --forest-mid: #6a5a3a;
    --forest-light: #b29a6a;
    --boar-dark: #2b2520;
    --boar-mid: #5e534a;
    --boar-light: #857768;
  }
  * { box-sizing: border-box; margin: 0; padding: 0; }
  html, body { width: 874px; height: 1200px; overflow: hidden; }
  body {
    background: var(--page-bg);
    font-family: "Open Sans", Arial, sans-serif;
    position: relative;
  }
  .brochure-spread {
    position: absolute;
    left: 17px; top: 270px;
    width: 840px; height: 630px;
    display: grid;
    grid-template-columns: repeat(3, 1fr);
    box-shadow: 0 6px 18px rgba(0,0,0,.25);
  }
  .panel {
    position: relative;
    background: var(--panel-black);
    color: var(--text-light);
    padding: 26px 24px;
    font-size: 9.6px;
    line-height: 1.5;
    border-right: 1px solid var(--panel-edge);
    overflow: hidden;
  }
  .panel:last-child { border-right: none; }
  .panel-heading {
    font-style: italic;
    font-weight: 700;
    color: var(--text-heading);
    font-size: 11px;
    margin-bottom: 6px;
  }
  .panel-title { font-size: 12px; text-align: center; }
  .panel-subtitle { font-style: italic; text-align: center; margin-bottom: 12px; }
  .panel p { margin-bottom: 12px; }
  .feature-list, .species-list { list-style: none; margin-bottom: 12px; }
  .feature-list li::before { content: "• "; }
  .testimonial { font-style: italic; margin-bottom: 4px; }
  .testimonial-author { font-style: italic; color: var(--text-muted); margin-bottom: 12px; }
  .offer { font-weight: 600; font-style: italic; }
  .species-heading { font-weight: 700; color: var(--text-heading); margin-bottom: 4px; }
  .fine-print { font-style: italic; color: var(--text-muted); }
  .photo-placeholder {
    position: absolute;
    background: linear-gradient(160deg, var(--boar-light) 0%, var(--boar-mid) 45%, var(--boar-dark) 100%);
    border: 1px solid #3a332d;
  }
  .photo-boar { left: 24px; right: 24px; top: 380px; height: 190px; }
  .photo-boar-pair { left: 24px; right: 24px; top: 430px; height: 160px; }
  .photo-hunter {
    height: 170px; margin: -26px -24px 18px;
    background: linear-gradient(100deg, var(--forest-dark) 0%, var(--forest-mid) 40%, var(--forest-light) 70%, var(--forest-mid) 100%);
  }
</style>
</head>
<body>
  <main class="brochure-spread">
    <section class="panel panel-intro">
      <h1 class="panel-heading panel-title">Montrez votre côté rebelle!</h1>
      <p class="panel-subtitle">Offrez-vous LE trip de chasse entre amis !</p>
      <p>Chassez en tout temps et sans permis sur deux magnifiques territoires forestiers de la taille de 30 terrains de football chacun. Les enclos sont situés en Beauce, à 30 minutes de Québec. Le taux de succès est de 100 %. Nous pouvons aussi fournir l'hébergement sur demande. La ferme est ouverte depuis 1982 et a toujours été gérée par des passionnés de la chasse, de la nature et de la bonne venaison.</p>
      <h2 class="panel-heading">C'est presque « hors-la-loi »!</h2>
      <ul class="feature-list">
        <li>Aucun permis requis</li>
        <li>Succès garanti</li>
        <li>Chasse pendant toute l'année</li>
        <li>Guide sur place et territoire exclusif</li>
        <li>À proximité de Québec</li>
      </ul>
      <div class="photo-placeholder photo-boar" role="img" aria-label="Photo d'un sanglier debout, de profil, sur fond noir"></div>
    </section>

    <section class="panel panel-hunt">
      <div class="photo-hunter" role="img" aria-label="Photo d'un chasseur en forêt"></div>
      <h2 class="panel-heading">Intense et renversant!</h2>
      <p>Que vous soyez un chasseur débutant ou vétéran, la chasse au sanglier sera pour vous une expérience extraordinaire. Ce gibier, qui ne vit pas à l'état sauvage au Québec, est un adversaire de taille. Ne vous fiez pas à son allure tranquille. S'il se sent en danger, il n'hésite pas à se sauver à toute vitesse et il n'arrête pas, même si vous vous trouvez sur son chemin. Ce gibier est suffisamment gros pour être chassé avec la plupart des carabines. Il se prête aussi très bien à la chasse au fusil, à l'arc ou à l'arbalète.</p>
      <h2 class="panel-heading">C'est bien beau, mais ça goûte quoi?</h2>
      <p>La chair du sanglier est rouge et elle est plus maigre que celle du porc. Elle est très tendre et succulente. Le sanglier offre les mêmes possibilités de coupe que le porc. Vous pouvez aussi l'essayer en méchoui à l'occasion d'une rencontre de groupe. Vos convives et vous dégusterez alors une venaison exceptionnelle.</p>
    </section>

    <section class="panel panel-reviews">
      <h2 class="panel-heading">Quelques commentaires de nos chasseurs :</h2>
      <p class="testimonial">« J'ai été surpris de voir à quel point ces animaux peuvent se cacher et se déplacer rapidement. C'est beaucoup plus difficile que je croyais. »</p>
      <p class="testimonial-author">Gaston, Québec, 2015</p>
      <p class="testimonial">« La viande était succulente et tendre. J'ai hâte de revenir récolter un autre sanglier à la ferme. »</p>
      <p class="testimonial-author">Brigitte, Québec, 2015</p>
      <p class="offer">Réservez pendant le salon et obtenez le crâne blanchi de votre sanglier gratuitement.</p>
      <p class="species-heading">Venez récolter les espèces exotiques suivantes :</p>
      <ul class="species-list">
        <li>Cerf de Virginie (500 $*)</li>
        <li>Cerf élaphe (850 $*)</li>
        <li>Sika (600 $*)</li>
        <li>Daim (500 $*)</li>
        <li>Dindon sauvage (85 $*)</li>
        <li>Faisan (200 $ pour 10)</li>
        <li>Sanglier (350 $*)</li>
      </ul>
      <p class="fine-print">*Prix de départ, sujet à changement sans préavis.</p>
      <div class="photo-placeholder photo-boar-pair" role="img" aria-label="Photo de deux sangliers côte à côte sur fond noir"></div>
    </section>
  </main>
</body>
</html>
```